Custom unique Stationary design for Logistics company

We need a custom, unique , elegant and luxurious full stationary design using our new logo, following these guidelines:
1- Business card: double sided, both sides uses the navy blue as the background main color (same as the code of the navy blue used in our logo).
2- envelope and folder: also use the same navy blue as the main background color.
3- book cover( notepad cover) : same thing with the navy blue
4- letterhead: feel free to use the combination of the colors in our logo.
5- rest of the items are up to your creativity

Target Market(s)

corporates and other businesses

Industry/Entity Type

Logistics and heavy machines contractors

Requirements
Must have
• Letterhead, business card, envelope, notepad cover, paper, file
Nice to have
• navy blue to be main background color for business card, envelope, notepad cover

```html
<!DOCTYPE html>
<html lang="en">
<head>
<meta charset="utf-8">
<title>Harbor Ridge Logistics – Business Card</title>
<link href="https://fonts.googleapis.com/css2?family=Archivo:wght@700&family=Karla:wght@400;700&display=swap" rel="stylesheet">
<style>
  :root {
    --backdrop: #2b2b2d;
    --navy: #235279;
    --navy-deep: #1b4465;
    --orange: #f05a22;
    --white: #ffffff;
    --grey: #a9adb3;
    --brand-blue: #2f9ad6;
  }
  * { box-sizing: border-box; margin: 0; padding: 0; }
  html, body { width: 1200px; height: 874px; overflow: hidden; background: var(--backdrop); }
  .canvas { position: relative; width: 1200px; height: 874px; }

  .card {
    position: absolute;
    width: 560px; height: 320px;
    background: var(--navy);
    border-radius: 14px;
    overflow: hidden;
    font-family: "Karla", sans-serif;
    color: var(--white);
  }
  .card--front { left: 470px; top: 60px; }
  .card--back  { left: 170px; top: 460px; }

  /* front */
  .front-brand {
    position: absolute; inset: 0;
    display: flex; align-items: center; justify-content: center; gap: 14px;
  }
  .front-brand__dot { width: 18px; height: 18px; border-radius: 50%; background: var(--orange); }
  .front-brand__name { font-weight: 700; font-size: 38px; color: var(--brand-blue); letter-spacing: .5px; }

  /* back */
  .person { position: absolute; left: 38px; top: 78px; }
  .person__name { font-family: "Archivo", sans-serif; font-weight: 700; font-size: 21px; color: var(--orange); text-transform: uppercase; letter-spacing: -.2px; }
  .person__title { font-size: 14px; margin-top: 2px; }

  .contacts { position: absolute; left: 38px; top: 142px; list-style: none; font-size: 14px; line-height: 21px; }
  .contacts li { display: flex; align-items: center; gap: 9px; }
  .contacts svg { width: 11px; height: 11px; fill: var(--orange); flex: none; }

  .divider { position: absolute; left: 30px; top: 216px; width: 290px; height: 1px; background: var(--orange); }

  .back-brand { position: absolute; right: 42px; top: 70px; display: flex; align-items: center; gap: 10px; }
  .back-brand__dot { width: 12px; height: 12px; border-radius: 50%; background: var(--orange); }
  .back-brand__name { font-weight: 700; font-size: 26px; color: var(--white); }

  .office { position: absolute; right: 98px; top: 180px; text-align: right; font-size: 14px; line-height: 18px; font-style: normal; }
  .office__company { color: var(--orange); font-size: 15px; padding-bottom: 4px; margin-bottom: 5px; border-bottom: 1px solid var(--orange); }

  .footer-band { position: absolute; left: 0; bottom: 0; width: 560px; height: 60px; }
  .website {
    position: absolute; left: 326px; bottom: 6px; width: 210px; height: 40px;
    display: flex; align-items: center; justify-content: center;
    font-size: 13px; letter-spacing: 3px; color: var(--white); white-space: nowrap;
  }
</style>
</head>
<body>
<main class="canvas">

  <section class="card card--front" aria-label="Business card front">
    <div class="front-brand">
      <span class="front-brand__dot"></span>
      <span class="front-brand__name">Harbor Ridge Logistics</span>
    </div>
  </section>

  <section class="card card--back" aria-label="Business card back">
    <div class="person">
      <p class="person__name">Daniel Rivers</p>
      <p class="person__title">President</p>
    </div>

    <ul class="contacts">
      <li><svg viewBox="0 0 24 24"><path d="M6.6 10.8a15 15 0 0 0 6.6 6.6l2.2-2.2a1 1 0 0 1 1-.25 11.4 11.4 0 0 0 3.6.57 1 1 0 0 1 1 1V20a1 1 0 0 1-1 1A17 17 0 0 1 3 4a1 1 0 0 1 1-1h3.5a1 1 0 0 1 1 1c0 1.250.2 2.45.57 3.57a1 1 0 0 1-.25 1z"/></svg>555-201-7734</li>
      <li><svg viewBox="0 0 24 24"><path d="M7 1h10a2 2 0 0 1 2 2v18a2 2 0 0 1-2 2H7a2 2 0 0 1-2-2V3a2 2 0 0 1 2-2zm0 3v15h10V4z"/></svg>555-309-4412</li>
      <li><svg viewBox="0 0 24 24"><path d="M2 4h20v16H2zm2 2v.5l8 5 8-5V6zm0 2.8V18h16V8.8l-8 5z"/></svg>daniel@harborridge.com</li>
    </ul>

    <div class="divider"></div>

    <div class="back-brand">
      <span class="back-brand__dot"></span>
      <span class="back-brand__name">Harbor Ridge</span>
    </div>

    <address class="office">
      <p class="office__company">Harbor Ridge Logistics</p>
      <p>1420 Tidewater Road</p>
      <p>Kodiak, Alaska 99615</p>
    </address>

    <svg class="footer-band" viewBox="0 0 560 60" aria-hidden="true">
      <rect x="0" y="44" width="560" height="16" fill="var(--grey)"/>
      <rect x="0" y="40" width="400" height="5" fill="var(--white)"/>
      <path d="M400 60 V22 Q400 6 416 6 H560 V60 Z" fill="var(--white)"/>
      <rect x="326" y="14" width="210" height="40" rx="20" fill="var(--orange)"/>
      <path d="M2 32 l6 -5 v3 l-3 2 3 2 v3 z M10 32 l6 -5 v3 l-3 2 3 2 v3 z" fill="var(--orange)"/>
      <path d="M544 29 l6 5 -6 5 v-3 l3 -2 -3 -2 z" fill="var(--orange)"/>
    </svg>
    <p class="website">www.harborridge.com</p>
  </section>

</main>
</body>
</html>
```